RM BIZ CARDS

Hi,

Is it possible to see a one sided version (with logo and info) as well as a two-sided version (front side w/logo and back side with info)?
How do we choose card stock and finish once we approve a design?

We would like the following info included:

Peter Lowell
Rosfeld Talent Media
4127 Marwick Lane, Suite 300
Los Angeles, CA 90041
(323) 555-0148
peter@rosfeldtalentmedia.example

```html
<!DOCTYPE html>
<html lang="en">
<head>
<meta charset="utf-8">
<title>Rosfeld Talent Media — Business Card</title>
<link rel="stylesheet" href="https://fonts.googleapis.com/css2?family=Raleway:wght@300;400&display=swap">
<style>
  :root {
    --backdrop: #2a241d;
    --card-dark: #0b0b0b;
    --card-mid: #1f1f1f;
    --card-sheen: #3a3a3a;
    --ink: #f2f2f2;
    --ink-soft: #bdbdbd;
    --ink-muted: #8e8e8e;
  }
  * { margin: 0; padding: 0; box-sizing: border-box; }
  html, body {
    width: 1200px;
    height: 1023px;
    overflow: hidden;
    background: var(--backdrop);
  }
  .stage {
    position: relative;
    width: 1200px;
    height: 1023px;
    display: flex;
    align-items: center;
    justify-content: center;
  }
  .business-card {
    position: relative;
    width: 880px;
    height: 503px;
    border-radius: 20px;
    background: linear-gradient(115deg, var(--card-dark) 0%, var(--card-mid) 38%, var(--card-sheen) 50%, var(--card-mid) 60%, var(--card-dark) 100%);
    box-shadow: 0 18px 40px rgba(0,0,0,0.55);
    font-family: "Raleway", sans-serif;
    color: var(--ink);
    overflow: hidden;
  }
  .brand {
    position: absolute;
    left: 70px;
    top: 140px;
    display: flex;
    flex-direction: column;
    align-items: flex-start;
    gap: 34px;
  }
  .brand-mark {
    width: 84px;
    height: 84px;
    border: 3px solid var(--ink);
    border-radius: 50%;
  }
  .brand-name {
    font-weight: 300;
    font-size: 38px;
    letter-spacing: 3px;
    text-transform: uppercase;
    color: var(--ink);
    line-height: 1;
  }
  .contact {
    position: absolute;
    left: 500px;
    top: 120px;
  }
  .contact-name {
    font-weight: 300;
    font-size: 34px;
    letter-spacing: 1px;
    text-transform: uppercase;
    line-height: 1;
  }
  .contact-title {
    margin-top: 8px;
    font-size: 15px;
    color: var(--ink-muted);
  }
  .contact-lines {
    margin-top: 26px;
    list-style: none;
    font-size: 17px;
    color: var(--ink-soft);
    line-height: 1.75;
  }
  .contact-lines .with-icon {
    display: flex;
    align-items: center;
    gap: 10px;
  }
  .contact-lines svg {
    width: 13px;
    height: 13px;
    fill: var(--ink-soft);
    flex: none;
  }
</style>
</head>
<body>
<main class="stage">
  <article class="business-card">
    <div class="brand">
      <span class="brand-mark" aria-hidden="true"></span>
      <span class="brand-name">Rosfeld Talent</span>
    </div>
    <section class="contact">
      <h1 class="contact-name">Peter Lowell</h1>
      <p class="contact-title">Director</p>
      <ul class="contact-lines">
        <li>4127 Marwick Lane, Suite 300</li>
        <li>Los Angeles, CA 90041</li>
        <li class="with-icon">
          <svg viewBox="0 0 16 16" aria-hidden="true"><path d="M3.6 1.2 5.8 1l1.3 3.3-1.6 1.2a9 9 0 0 0 5 5l1.2-1.6L15 10.2l-.2 2.2c-.1.9-.9 1.6-1.8 1.6C6.7 14 2 9.3 2 3c0-.9.7-1.7 1.6-1.8Z"/></svg>
          (323) 555-0148
        </li>
        <li class="with-icon">
          <svg viewBox="0 0 16 16" aria-hidden="true"><path d="M1 3h14v10H1V3Zm1.5 1.5v.3L8 8.6l5.5-3.8v-.3h-11Zm11 2.1L8 10.4 2.5 6.6v4.9h11V6.6Z"/></svg>
          peter@rosfeldtalentmedia.example
        </li>
      </ul>
    </section>
  </article>
</main>
</body>
</html>
```